Package Design - Disposable Face Towel

Hi,

We are needing assistance with graphic design on our box/carton/package.

The attached image that is white is our biggest competitor.

Our brand is "BRIGHT DEW LTD." Please see the logo we uploaded.

Oder we have in mind for front of box:

Logo
LARGE TOWELS
50 Count
Ultra Soft| 100% USDA Bio-Based|100% Eucalyptus Viscose | Vegan
BRIGHTDEWLTD.EXAMPLE

We like medium to dark blue on most of the box, with white and minimal hot pink or salmon. Something that is sharp, modern, and stands out from our competitors.

Box dimensions are: 6.25 x 5.25 x 4.75 inches

This will be 1 of many design projects.

Target Market(s)

Female Beauty Products

Font styles to use
Serif
Sans Serif

Colors
0054AA
0677BA
7BADD7
CADEEF
E8F1F8
EB3D1F
EC4F4E
F09395
F8D3D4
FCEDEE

Requirements
Must have
• Needs to look sharp and modern

```html
<!DOCTYPE html>
<html lang="en">
<head>
<meta charset="utf-8">
<title>Bright Dew Ltd. – Large Towels Carton</title>
<link rel="stylesheet" href="https://fonts.googleapis.com/css2?family=Marcellus&family=Josefin+Sans:wght@600&family=Libre+Baskerville&display=swap">
<style>
  :root {
    --navy: #1c3566;
    --navy-deep: #152a55;
    --band: #17367a;
    --salmon: #e86a6c;
    --salmon-dark: #c9474e;
    --white: #ffffff;
    --paper: #f4f4f6;
    --panel-grey: #eff0f3;
    --line-grey: #d9dbe1;
  }
  * { box-sizing: border-box; margin: 0; padding: 0; }
  html, body { width: 1200px; height: 2511px; overflow: hidden; background: var(--white); }
  .canvas { position: relative; width: 1200px; height: 2511px; }

  /* Flat wrap artwork */
  .wrap-sheet {
    position: absolute; left: 390px; top: 104px; width: 753px; height: 571px;
    background: var(--panel-grey);
  }
  .wrap-art {
    position: absolute; left: 77px; top: 0; width: 599px; height: 571px;
    background: radial-gradient(circle at 50% 50%, #213e75 0%, var(--navy) 60%, var(--navy-deep) 100%);
  }
  .logo-frame {
    position: absolute; border: 2px solid var(--white);
    display: flex; align-items: center; justify-content: center;
    font-family: "Marcellus", serif; color: var(--white); white-space: nowrap;
  }
  .wrap-art .logo-frame { left: 108px; top: 244px; width: 377px; height: 62px; font-size: 40px; letter-spacing: 0.5px; }
  .wrap-title {
    position: absolute; left: 0; right: 0; top: 325px; text-align: center;
    font-family: "Josefin Sans", sans-serif; font-weight: 600; font-size: 26px;
    color: var(--white); letter-spacing: 1px;
  }

  /* Flat carton front */
  .carton-front { position: absolute; left: 200px; top: 900px; width: 800px; height: 1100px; }
  .dispense-flap {
    position: absolute; left: 60px; top: 0; width: 680px; height: 380px;
    background: radial-gradient(circle at 50% 55%, #213e75 0%, var(--navy) 60%, var(--navy-deep) 100%);
  }
  .dispense-flap .logo-frame { left: 130px; top: 140px; width: 420px; height: 66px; font-size: 42px; }
  .front-panel {
    position: absolute; left: 0; top: 380px; width: 800px; height: 620px;
    background: var(--paper); border: 1px solid var(--line-grey);
  }
  .slot-outline {
    position: absolute; left: 40px; top: 24px; width: 720px; height: 84px;
    border: 2px solid var(--line-grey); border-radius: 42px;
  }
  .front-title {
    position: absolute; left: 0; right: 0; top: 190px; text-align: center;
    font-family: "Josefin Sans", sans-serif; font-weight: 600; font-size: 40px;
    color: var(--band); letter-spacing: 2.5px;
  }
  .feature-list {
    position: absolute; left: 0; right: 0; top: 290px; text-align: center;
    font-family: "Libre Baskerville", serif; font-size: 19px; line-height: 34px;
    color: var(--band); letter-spacing: 1.2px;
  }
  .web-band {
    position: absolute; left: 0; right: 0; bottom: 0; height: 74px;
    background: linear-gradient(90deg, var(--navy-deep), var(--band) 50%, var(--navy-deep));
    display: flex; align-items: center; justify-content: center;
    font-family: "Libre Baskerville", serif; font-size: 21px; letter-spacing: 3px; color: var(--white);
  }
  .count-badge { position: absolute; right: 40px; bottom: 30px; width: 110px; height: 110px; }
</style>
</head>
<body>
<main class="canvas">

  <section class="wrap-sheet">
    <div class="wrap-art" role="img" aria-label="Repeating illustrated pattern of dancing women, headphones and phones in salmon, white and periwinkle on navy">
      <div class="logo-frame">BRIGHT DEW LTD.</div>
      <p class="wrap-title">LARGE TOWELS</p>
    </div>
  </section>

  <section class="carton-front">
    <div class="dispense-flap" role="img" aria-label="Dispenser flap with navy illustrated pattern of dancing women">
      <div class="logo-frame">BRIGHT DEW LTD.</div>
    </div>
    <div class="front-panel">
      <div class="slot-outline"></div>
      <h1 class="front-title">LARGE TOWELS</h1>
      <p class="feature-list">Ultra Soft&nbsp;|&nbsp;100% USDA Bio–Based<br>100% Eucalyptus Viscose&nbsp;|&nbsp;Vegan</p>
      <div class="web-band">www.brightdewltd.example</div>
      <svg class="count-badge" viewBox="0 0 110 110" aria-label="50 Count">
        <rect x="22" y="22" width="66" height="66" rx="6" transform="rotate(45 55 55)" fill="var(--salmon-dark)" stroke="var(--white)" stroke-width="3"/>
        <text x="55" y="58" text-anchor="middle" font-family="Libre Baskerville, serif" font-size="24" fill="var(--white)">50</text>
        <text x="55" y="76" text-anchor="middle" font-family="Libre Baskerville, serif" font-size="12" fill="var(--white)">Count</text>
      </svg>
    </div>
  </section>

</main>
</body>
</html>
```